Business Card Design Project

I am a Chiropractor that is looking for a new business card.  Our logo was slightly changed lately, therefore need a new, more professional look.
We are a modern, non-stuffy chiropractic office.  Want a contemporary look that will let people know this is not your typical doctors office.  Our logo is red, and contains the name of our business: realign.  The u in the logo is green, stressing the most important part of our business: "u"

Target Market(s)
moderate to upper income bracket, family friendly
www.realignspine-example.com
Gordon Pell
Family Chiropractor
314 Hollis Rd
Elmridge, OR 97999
555.555.0147 phone
555.555.0148 fax
Industry/Entity Type
Business
Requirements
Must have
- www.realignspine-example.com
Gordon Pell
Family Chiropractor
314 Hollis Rd
Elmridge, OR 97999
555.555.0147 phone
555.555.0148 fax

```html
<!DOCTYPE html>
<html lang="en">
<head>
<meta charset="utf-8">
<title>realign — Business Card</title>
<link rel="stylesheet" href="https://fonts.googleapis.com/css2?family=Open+Sans:wght@300;400;700&display=swap">
<style>
  :root {
    --bg: #efe9e2;
    --ink: #0b0b0b;
    --paper: #ffffff;
    --red: #e8403a;
    --red-deep: #c9302b;
    --green: #6ab344;
    --text: #1c1c1c;
  }
  * { margin: 0; padding: 0; box-sizing: border-box; }
  html, body {
    width: 1200px; height: 900px; overflow: hidden;
    background: var(--bg);
    font-family: "Open Sans", Arial, sans-serif;
  }
  .stage {
    position: relative; width: 1200px; height: 900px;
    display: flex; align-items: center; justify-content: center; gap: 50px;
  }
  .card {
    position: relative; width: 530px; height: 306px;
    border-radius: 24px; overflow: hidden;
    box-shadow: 0 6px 18px rgba(0,0,0,.18);
  }

  /* Back side */
  .card--back { background: var(--ink); }
  .card--back .brand {
    position: absolute; left: 0; right: 0; top: 104px;
    display: flex; align-items: center; justify-content: center; gap: 14px;
  }
  .brand__dot {
    width: 22px; height: 22px; border-radius: 50%; background: var(--red);
  }
  .brand__name {
    font-weight: 300; font-size: 56px; letter-spacing: 1px;
    color: var(--red); line-height: 1;
  }
  .card--back .site {
    position: absolute; left: 0; right: 0; top: 206px;
    text-align: center; font-size: 17px; letter-spacing: .3px;
    color: var(--red);
  }
  .site__domain { color: var(--green); }

  /* Front side */
  .card--front { background: var(--paper); }
  .card--front .wave { position: absolute; inset: 0; }
  .card--front .brand {
    position: absolute; left: 40px; top: 108px;
    display: flex; align-items: center; gap: 10px;
  }
  .card--front .brand__dot { width: 16px; height: 16px; }
  .card--front .brand__name { font-size: 42px; }
  .contact {
    position: absolute; left: 350px; top: 52px; color: var(--text);
  }
  .contact__name {
    font-weight: 700; font-size: 23px; line-height: 1.1; color: var(--red);
  }
  .contact__name .surname { color: var(--green); }
  .contact__role {
    font-weight: 700; font-size: 13px; margin-top: 3px; margin-bottom: 12px;
  }
  .contact__list { list-style: none; font-size: 13px; }
  .contact__list li {
    display: flex; align-items: center; gap: 8px; height: 22px;
  }
  .contact__list li.indent { padding-left: 28px; }
  .icon { width: 20px; height: 20px; flex: none; }
  .card--front .site {
    position: absolute; left: 40px; bottom: 26px;
    font-size: 13px; color: var(--text); letter-spacing: .2px;
  }
</style>
</head>
<body>
<main class="stage">

  <section class="card card--back" aria-label="Card back">
    <div class="brand">
      <span class="brand__dot"></span>
      <span class="brand__name">realign</span>
    </div>
    <p class="site">www.<span class="site__domain">realignspine-example</span>.com</p>
  </section>

  <section class="card card--front" aria-label="Card front">
    <svg class="wave" viewBox="0 0 530 306" width="530" height="306" aria-hidden="true">
      <path d="M0 0 H318 C292 100 220 190 0 252 Z" fill="var(--ink)"/>
      <path d="M318 0 C292 100 220 190 0 252" fill="none" stroke="var(--red-deep)" stroke-width="6"/>
      <path d="M332 0 C304 104 230 198 0 262" fill="none" stroke="var(--green)" stroke-width="8"/>
      <path d="M346 0 C318 108 242 204 0 272" fill="none" stroke="var(--red)" stroke-width="4"/>
    </svg>

    <div class="brand">
      <span class="brand__dot"></span>
      <span class="brand__name">realign</span>
    </div>

    <div class="contact">
      <h1 class="contact__name">Gordon <span class="surname">Pell</span></h1>
      <p class="contact__role">Family Chiropractor</p>
      <ul class="contact__list">
        <li>
          <svg class="icon" viewBox="0 0 20 20" aria-label="Phone"><circle cx="10" cy="10" r="9" fill="var(--red)"/><path d="M7 5.5l1.8 2.2-1 1.2c.6 1.3 1.6 2.3 2.9 2.9l1.2-1 2.2 1.8-.9 1.6c-3.8-.3-6.9-3.4-7.2-7.2z" fill="#fff"/></svg>
          555.555.0147
        </li>
        <li>
          <svg class="icon" viewBox="0 0 20 20" aria-label="Fax"><circle cx="10" cy="10" r="9" fill="var(--red)"/><rect x="6" y="7" width="8" height="6" rx="1" fill="#fff"/><rect x="7.5" y="5" width="5" height="2" fill="#fff"/></svg>
          555.555.0148
        </li>
        <li>
          <svg class="icon" viewBox="0 0 20 20" aria-label="Address"><circle cx="10" cy="10" r="9" fill="var(--red)"/><path d="M10 5l5 4.5h-1.5V14h-2.5v-3H9v3H6.5V9.5H5z" fill="#fff"/></svg>
          314 Hollis Rd
        </li>
        <li class="indent">Elmridge, OR 97999</li>
      </ul>
    </div>

    <p class="site">www.realignspine-example.com</p>
  </section>

</main>
</body>
</html>
```